Auto glazing business card design

need a business card design for my company, the logo will be provided with an inspirational design as well.
It is for an auto glazing business in Australia.
I would like to have the basic details on the card as my name, phone number, email adress and website.
I suppose the challenge will be to fit a long email adress on a small business card.

Target Market(s)

autoglazing customers, retail mostly

Industry/Entity Type

auto glazing

Contact Information for Business Card

logo, name, phone, email and website

Colors
0054AA
0677BA
7BADD7
CADEEF
E8F1F8
0094D4
00A9DD
6FCCEA
C7EBF8
E9F6FB

Requirements
Must have
• logo, business details, maybe QR code

```html
<!DOCTYPE html>
<html lang="en">
<head>
<meta charset="utf-8">
<title>Clearview Mobile Services – Business Card</title>
<link href="https://fonts.googleapis.com/css2?family=Poppins:wght@400;500;600&display=swap" rel="stylesheet">
<style>
  :root {
    --stage: #2b3038;
    --card-white: #ffffff;
    --card-navy: #0b1f3a;
    --ink-navy: #0f1c30;
    --ink-body: #2a2f38;
    --accent-blue: #0094d4;
    --accent-cyan: #00a9dd;
    --wordmark-light: #c9ced6;
  }
  * { box-sizing: border-box; margin: 0; padding: 0; }
  html, body {
    width: 1200px; height: 985px; overflow: hidden;
    background: var(--stage);
    font-family: "Poppins", sans-serif;
  }
  .sheet {
    width: 1200px; height: 985px;
    display: flex; flex-direction: column;
    align-items: center; justify-content: center; gap: 50px;
  }
  .card {
    position: relative;
    width: 680px; height: 390px;
    border-radius: 30px;
    border: 4px solid var(--accent-cyan);
    overflow: hidden;
  }
  .card--front { background: var(--card-white); }
  .card--back {
    background: var(--card-navy);
    display: flex; align-items: center; justify-content: center;
  }

  .wordmark {
    display: flex; align-items: center; gap: 12px;
    font-weight: 600; font-size: 30px; line-height: 1.1;
    color: var(--ink-navy);
  }
  .wordmark__dot {
    width: 16px; height: 16px; border-radius: 50%;
    background: var(--accent-blue); flex: none;
  }
  .card--front .wordmark { position: absolute; right: 44px; top: 64px; }
  .card--back .wordmark { color: var(--wordmark-light); font-size: 34px; }

  .holder { position: absolute; left: 44px; top: 170px; }
  .holder__name {
    font-weight: 600; font-size: 20px; letter-spacing: 0.02em;
    color: var(--ink-body); text-transform: uppercase;
  }
  .holder__role { font-size: 15px; color: var(--accent-blue); margin-top: 2px; }

  .divider {
    position: absolute; left: 44px; top: 242px;
    width: 560px; height: 2px; background: var(--accent-blue);
  }

  .contacts {
    position: absolute; left: 44px; top: 260px;
    list-style: none; display: flex; flex-direction: column; gap: 8px;
  }
  .contacts li {
    display: flex; align-items: center; gap: 10px;
    font-size: 14px; color: var(--ink-body);
  }
  .contacts svg { width: 14px; height: 14px; flex: none; }
  .icon-fill { fill: var(--accent-blue); }
  .icon-line { fill: none; stroke: var(--accent-blue); }
</style>
</head>
<body>
<main class="sheet">
  <section class="card card--front" aria-label="Card front">
    <p class="wordmark"><span class="wordmark__dot"></span>Clearview Mobile Services</p>

    <div class="holder">
      <p class="holder__name">Daniel Harper</p>
      <p class="holder__role">Manager</p>
    </div>

    <div class="divider"></div>

    <ul class="contacts">
      <li>
        <svg viewBox="0 0 24 24" aria-hidden="true"><path class="icon-fill" d="M6.6 10.8a15.1 15.1 0 0 0 6.6 6.6l2.2-2.2a1 1 0 0 1 1-.25 11.4 11.4 0 0 0 3.6.57 1 1 0 0 1 1 1V20a1 1 0 0 1-1 1A17 17 0 0 1 3 4a1 1 0 0 1 1-1h3.5a1 1 0 0 1 1 1c0 1.25.2 2.45.57 3.57a1 1 0 0 1-.25 1z"/></svg>
        555-018-2740
      </li>
      <li>
        <svg viewBox="0 0 24 24" aria-hidden="true"><path class="icon-line" stroke-width="2.4" d="M2 5h20v14H2z M2 5l10 8 10-8"/></svg>
        hello@clearviewmobile.com.au
      </li>
      <li>
        <svg viewBox="0 0 24 24" aria-hidden="true"><circle class="icon-line" stroke-width="2" cx="12" cy="12" r="10"/><path class="icon-line" stroke-width="1.6" d="M2 12h20M12 2c3 3 3 17 0 20M12 2c-3 3-3 17 0 20"/></svg>
        www.clearviewmobile.com.au
      </li>
    </ul>
  </section>

  <section class="card card--back" aria-label="Card back">
    <p class="wordmark">Clearview Mobile Services</p>
  </section>
</main>
</body>
</html>
```